Big Bear Lake Visitor Guide Ad

We need a fresh design for a full page ad in our community's Visitors Guide. We are a Vacation Rental Company in a 4 season resort town. We'd like the ad to focus on winter but incorporate the other 3 seasons, as the guide is for the entire year. Our slogan is "Great Vacations Start Here!" and our colors are Blue and gold. The final design should communicate fun and family.

Target Market(s)

Southern California families and active adults

Industry/Entity Type

It Company

Requirements
Must have
• Logo, phone number, activities, website address. Ridgetopfernlodges.com
• slogan "Great Vacations Start Here!". 4 color ad

```html
<!DOCTYPE html>
<html lang="en">
<head>
<meta charset="utf-8">
<title>Ridgetop Fern Lodges – Visitor Guide Ad</title>
<link rel="stylesheet" href="https://fonts.googleapis.com/css2?family=Cinzel:wght@400;700&family=Libre+Baskerville:wght@400;700&display=swap">
<style>
  :root {
    --charcoal: #2c2e33;
    --charcoal-deep: #232529;
    --gold: #f4b41a;
    --blue: #1f8fd0;
    --blue-dark: #1a4f8c;
    --white: #ffffff;
    --ink: #1f3a63;
  }
  * { margin: 0; padding: 0; box-sizing: border-box; }
  html, body { width: 870px; height: 1200px; overflow: hidden; background: var(--white); }
  .ad {
    position: relative;
    width: 870px;
    height: 1200px;
    overflow: hidden;
    background: var(--charcoal);
    font-family: "Libre Baskerville", Georgia, serif;
  }
  .ad-art { position: absolute; inset: 0; }
  .brand {
    position: absolute;
    left: 46px;
    top: 46px;
    display: flex;
    align-items: center;
    gap: 14px;
  }
  .brand-name {
    font-family: "Cinzel", Georgia, serif;
    font-weight: 700;
    font-size: 38px;
    line-height: 1.05;
    color: var(--ink);
    letter-spacing: 1px;
  }
  .brand-mark {
    width: 34px; height: 34px;
    background: var(--gold);
    transform: rotate(45deg);
    flex: none;
  }
  .slogan {
    position: absolute;
    left: 52px;
    top: 700px;
    font-family: "Cinzel", Georgia, serif;
    font-weight: 700;
    line-height: 1;
  }
  .slogan-lead { display: block; color: var(--white); font-size: 48px; letter-spacing: 1px; }
  .slogan-punch { display: block; color: var(--gold); font-size: 66px; margin-top: 10px; }
  .activities {
    position: absolute;
    left: 52px;
    top: 858px;
    width: 780px;
    color: var(--white);
  }
  .activities-title { font-size: 34px; font-weight: 400; margin-bottom: 16px; }
  .activities-list {
    list-style: none;
    display: grid;
    grid-template-columns: 250px 200px 130px auto;
    grid-auto-flow: column;
    grid-template-rows: repeat(4, 28px);
    font-size: 15px;
  }
  .activities-list li { position: relative; padding-left: 18px; white-space: nowrap; }
  .activities-list li::before {
    content: ""; position: absolute; left: 0; top: 6px;
    width: 8px; height: 8px; background: var(--gold); border-radius: 50%;
  }
  .activities-list li.more { grid-column: 4; grid-row: 4; padding-left: 0; }
  .activities-list li.more::before { display: none; }
  .contact {
    position: absolute;
    left: 0; right: 0; bottom: 0;
    height: 78px;
    background: var(--white);
    display: flex;
    align-items: center;
    justify-content: space-between;
    padding: 0 60px 0 52px;
    font-family: "Libre Baskerville", Georgia, serif;
    font-weight: 700;
    font-size: 27px;
    color: var(--charcoal-deep);
  }
  .contact-item { display: flex; align-items: center; gap: 12px; white-space: nowrap; }
  .contact-item svg { width: 28px; height: 28px; }
</style>
</head>
<body>
<main class="ad">
  <svg class="ad-art" width="870" height="1200" viewBox="0 0 870 1200">
    <defs>
      <linearGradient id="bridgePhoto" x1="0" y1="0" x2="1" y2="1">
        <stop offset="0" stop-color="#8a8f8c"/>
        <stop offset="0.45" stop-color="#b9bcb6"/>
        <stop offset="1" stop-color="#d8d8d2"/>
      </linearGradient>
      <linearGradient id="sunsetPhoto" x1="0" y1="0" x2="0" y2="1">
        <stop offset="0" stop-color="#1b78c9"/>
        <stop offset="0.6" stop-color="#4aa6e0"/>
        <stop offset="1" stop-color="#f1a24a"/>
      </linearGradient>
      <linearGradient id="lodgePhoto" x1="0" y1="0" x2="1" y2="1">
        <stop offset="0" stop-color="#5b4638"/>
        <stop offset="0.6" stop-color="#8a5a3f"/>
        <stop offset="1" stop-color="#b22f38"/>
      </linearGradient>
      <linearGradient id="snowPhoto" x1="0" y1="0" x2="1" y2="1">
        <stop offset="0" stop-color="#e6ecf2"/>
        <stop offset="1" stop-color="#b8c6d6"/>
      </linearGradient>
    </defs>

    <g role="img" aria-label="Photo of a long wooden footbridge over a lake with pine trees">
      <path d="M0 0 H870 V450 C700 520 420 560 0 560 Z" fill="url(#bridgePhoto)"/>
    </g>
    <path d="M0 0 H580 C470 80 300 150 0 190 Z" fill="var(--white)"/>
    <path d="M0 190 C300 150 470 80 580 0 H610 C500 100 320 180 0 215 Z" fill="var(--gold)"/>
    <path d="M0 215 C320 180 500 100 610 0 H625 C510 115 330 195 0 228 Z" fill="var(--blue)"/>

    <path d="M0 560 C420 560 700 520 870 450 V480 C700 560 420 600 0 600 Z" fill="var(--gold)"/>
    <path d="M0 600 C420 600 700 560 870 480 V500 C700 585 420 625 0 625 Z" fill="var(--blue)"/>

    <g transform="translate(760 320) rotate(45)">
      <rect x="-112" y="-112" width="224" height="224" fill="var(--blue)"/>
      <rect x="-104" y="-104" width="208" height="208" fill="var(--white)"/>
      <rect x="-96" y="-96" width="192" height="192" fill="url(#sunsetPhoto)" role="img" aria-label="Photo of a bare tree silhouetted against a winter sunset"/>
    </g>
    <g transform="translate(560 560) rotate(45)">
      <rect x="-102" y="-102" width="204" height="204" fill="var(--blue)"/>
      <rect x="-95" y="-95" width="190" height="190" fill="var(--white)"/>
      <rect x="-88" y="-88" width="176" height="176" fill="url(#lodgePhoto)" role="img" aria-label="Photo of a cabin game room with a pool table"/>
    </g>
    <g transform="translate(740 760) rotate(45)">
      <rect x="-112" y="-112" width="224" height="224" fill="var(--blue)"/>
      <rect x="-104" y="-104" width="208" height="208" fill="var(--white)"/>
      <rect x="-96" y="-96" width="192" height="192" fill="url(#snowPhoto)" role="img" aria-label="Photo of a family playing together in the snow"/>
    </g>
    <rect x="-40" y="-40" width="80" height="80" fill="var(--gold)" transform="translate(872 520) rotate(45)"/>
    <rect x="-40" y="-40" width="80" height="80" fill="var(--gold)" transform="translate(560 700) rotate(45)"/>
  </svg>

  <div class="brand">
    <span class="brand-mark"></span>
    <span class="brand-name">Ridgetop<br>Fern Lodges</span>
  </div>

  <h1 class="slogan">
    <span class="slogan-lead">Great Vacations</span>
    <span class="slogan-punch">Start Here!</span>
  </h1>

  <section class="activities">
    <h2 class="activities-title">Activities:</h2>
    <ul class="activities-list">
      <li>Alpine slide &amp; water slide</li>
      <li>Biking</li>
      <li>Boating &amp; water sports</li>
      <li>Fishing</li>
      <li>Gun Range</li>
      <li>Helicopter flights</li>
      <li>Hiking</li>
      <li>Horse back riding</li>
      <li>Parasailing</li>
      <li>Off-roading</li>
      <li>Tennis</li>
      <li>Waterskiing</li>
      <li class="more">...and many more</li>
    </ul>
  </section>

  <footer class="contact">
    <span class="contact-item">
      <svg viewBox="0 0 24 24" aria-hidden="true"><circle cx="12" cy="12" r="11" fill="none" stroke="var(--charcoal-deep)" stroke-width="2"/><path d="M8.5 6.5l2 2-1.2 1.6c.7 1.6 2 2.9 3.6 3.6l1.6-1.2 2 2-1.3 1.8c-4-.6-7.9-4.5-8.5-8.5z" fill="var(--charcoal-deep)"/></svg>
      800-555-0142
    </span>
    <span class="contact-item">
      <svg viewBox="0 0 24 24" aria-hidden="true"><circle cx="12" cy="12" r="10" fill="none" stroke="var(--charcoal-deep)" stroke-width="2"/><ellipse cx="12" cy="12" rx="4.5" ry="10" fill="none" stroke="var(--charcoal-deep)" stroke-width="1.6"/><path d="M2 12h20" stroke="var(--charcoal-deep)" stroke-width="1.6"/></svg>
      www.ridgetopfernlodges.com
    </span>
  </footer>
</main>
</body>
</html>
```